Infographic Design for Aluminium Can Recycling

We require a neat design that can be integrated into print advertising for a 'cash for cans' recycling promotion and also scaled back for Chatterloop promotion. The promotion is aimed at kids/families. Needs to be fresh and colourful - but also appealing to children. The flyer is to be designed at A5 size and also at CL post sizing. You can just submit the one design in A5 to win, with the knowledge that you will need to redesign slightly later to suit CL post size.

The design needs to contain as much of the following as possible.

- The best thing is - Aluminium is 100% recyclable FOREVER
- If you recycled just one can everyday for a week, you'd save enough energy to watch TV straight for 21 hours - thats an entire season of XXX
- 105,784 cans are recycled every minute
- it takes the same amount of energy to make 1 new can as it does to recycle 20
- a recycled can is back on the shelf in 60 days
-2/3 of the aluminium ever produced is still in use today

Please keep colours muted - not bright
Please do not present anything like the 'Blue Lantern' lie attached. This is far too busy.
I have attached the original flyer for information only (see below for what to and what NOT to include)
I've attached some cute graphics I think kids and adults will find appealing. Design something similar. The prize to be won is an electric scooter - perhaps they could be riding this.

They are giving away an electric Scooter (not Bike)

Please use Penbury Ore Services and LOGO

Please provide address and details of event as per flyer

Please leave out the following text:
HEY KIDS
WIN THIS BIKE
FIND US ON CL
LUCKY DOOR PRIZE + SAUSAGE SIZZLE
WE PAY CASH FOR CANS
Collect as many aluminium cans as you can and bring them to our can day and get paid for cash
Do not include the can man graphic

Please have information:
Event location
Win an Electric Scooter
Turn in your CANS for CASH

Great - can't wait to see what you creative geniuses come back with!!
Updates

None of these designs matched the brief. Im actually not sure what to do now?

Target Market(s)

Males 35+

Industry/Entity Type

Advertising

Font styles to use
Sans Serif

Colors
5c5c5c
0555a3
3276b5
b1b1b1
faa54b
fbf289
33a6d7
f04a50

Requirements
Must have
• Please read brief
Nice to have
• Please see brief
Should not have
• Please see brief

```html
<!DOCTYPE html>
<html lang="en">
<head>
<meta charset="utf-8">
<title>Win an Electric Scooter – Cans to Cash Flyer</title>
<link href="https://fonts.googleapis.com/css2?family=Quicksand:wght@400;500;600;700&display=swap" rel="stylesheet">
<style>
  :root {
    --sky-top: #55c4cf;
    --sky-mid: #8fd6df;
    --sky-low: #d6f0f3;
    --white: #ffffff;
    --olive: #c3c63c;
    --coral: #ee7470;
    --slate: #4a4b5e;
    --teal-deep: #3a9fa3;
    --grass: #a9b83a;
    --rock: #4d5459;
    --gold: #e8e45a;
    --ink: #ffffff;
  }
  * { box-sizing: border-box; margin: 0; padding: 0; }
  html, body { width: 1200px; height: 1000px; overflow: hidden; background: #ffffff; }
  body { position: relative; font-family: "Quicksand", sans-serif; color: var(--ink); }

  .flyer {
    position: absolute;
    width: 682px;
    height: 968px;
    overflow: hidden;
    background: linear-gradient(180deg, var(--sky-top) 0%, var(--sky-top) 30%, var(--sky-mid) 55%, var(--sky-low) 78%);
  }
  .flyer--large { left: 478px; top: 20px; }
  .flyer--small { left: 50px; top: 417px; transform: scale(0.5806); transform-origin: top left; }

  .flyer__sparkle {
    position: absolute; left: 0; top: 0; width: 682px; height: 220px;
    background: radial-gradient(ellipse at 70% 40%, rgba(255,255,255,0.28), rgba(255,255,255,0) 70%);
  }

  .headline__win {
    position: absolute; left: 118px; top: 18px;
    font-size: 138px; font-weight: 500; letter-spacing: 6px; line-height: 1;
  }
  .headline__prize {
    position: absolute; left: 120px; top: 150px;
    font-size: 35px; font-weight: 600; letter-spacing: 2.5px; line-height: 1;
  }
  .headline__scooter {
    position: absolute; left: 440px; top: 25px; width: 120px; height: 112px;
    border-radius: 14px;
    background: rgba(255,255,255,0.85);
  }

  .fact {
    position: absolute; font-size: 10.5px; font-weight: 500; line-height: 1.3; letter-spacing: 0.6px;
  }
  .fact--right { text-align: right; }
  .fact-icon { position: absolute; }
  .fraction {
    position: absolute; left: 176px; top: 318px; width: 22px;
    text-align: center; font-size: 18px; font-weight: 700; color: var(--slate); line-height: 1.05;
  }
  .fraction span { display: block; }
  .fraction span:first-child { border-bottom: 2px solid var(--slate); }

  .cycle { position: absolute; left: 214px; top: 255px; }
  .cycle__text {
    position: absolute; left: 244px; top: 312px; width: 200px; text-align: center; line-height: 1;
  }
  .cycle__lead { font-size: 19px; font-weight: 600; letter-spacing: 1.5px; }
  .cycle__mid { font-size: 24px; font-weight: 600; letter-spacing: 1px; margin-top: 48px; }
  .cycle__cash { font-size: 40px; font-weight: 600; letter-spacing: 1px; margin-top: 4px; }
  .cycle__dollar { position: absolute; left: 84px; top: 30px; }

  .scene {
    position: absolute; left: 0; top: 740px; width: 682px; height: 228px;
    background: linear-gradient(180deg, #e9f6f7 0%, #e9f6f7 30%, var(--teal-deep) 42%, var(--teal-deep) 55%, var(--grass) 70%, #8d9a33 100%);
  }
  .scene__cliff {
    position: absolute; left: 360px; top: 740px; width: 322px; height: 120px;
    background: linear-gradient(180deg, var(--rock), #3d4347);
    clip-path: polygon(8% 0, 100% 0, 100% 100%, 20% 100%);
  }
  .character {
    position: absolute; left: 318px; top: 578px; width: 180px; height: 172px;
    border-radius: 12px;
    background: linear-gradient(180deg, rgba(80,110,150,0.35), rgba(40,150,200,0.45));
  }
  .coin-badge {
    position: absolute; left: 507px; top: 566px; width: 146px; height: 146px; border-radius: 50%;
    background: radial-gradient(circle, rgba(240,236,110,0.75), rgba(240,236,110,0.25) 70%);
  }

  .event {
    position: absolute; left: 17px; top: 672px; width: 353px; height: 143px;
    background: var(--coral); border-radius: 26px;
    padding: 24px 0 0 22px;
  }
  .event__row { display: flex; font-size: 14px; line-height: 18px; letter-spacing: 0.8px; }
  .event__label { width: 65px; font-weight: 700; }
  .event__value { font-weight: 500; }

  .brand {
    position: absolute; left: 55px; top: 900px; display: flex; align-items: center; gap: 8px;
  }
  .brand__mark { width: 26px; height: 26px; background: var(--white); }
  .brand__name { width: 70px; font-size: 9px; font-weight: 700; line-height: 1.1; letter-spacing: 0.5px; }
  .brand__call { display: flex; align-items: center; gap: 8px; margin-left: 8px; }
  .brand__local { font-size: 9.5px; font-weight: 700; line-height: 1.05; letter-spacing: 1px; }
  .brand__phone { font-size: 24px; font-weight: 700; letter-spacing: 1px; }
</style>
</head>
<body>

<!-- A5 flyer, reduced -->
<section class="flyer flyer--small" aria-label="Cans to cash flyer, small size">
  <div class="flyer__sparkle"></div>
  <div class="headline__win">WIN</div>
  <div class="headline__scooter" role="img" aria-label="Electric scooter illustration"></div>
  <div class="headline__prize">AN ELECTRIC SCOOTER</div>

  <p class="fact" style="left:88px;top:234px;">105,784 Cans Are<br>Recycled Every Minute</p>
  <svg class="fact-icon" style="left:226px;top:228px" width="40" height="40" viewBox="0 0 40 40" aria-hidden="true"><circle cx="20" cy="22" r="14" fill="none" stroke="#c3c63c" stroke-width="3"/><rect x="17" y="3" width="6" height="4" fill="#c3c63c"/><line x1="20" y1="22" x2="27" y2="15" stroke="#c3c63c" stroke-width="3"/></svg>

  <svg class="fact-icon" style="left:470px;top:274px" width="40" height="40" viewBox="0 0 40 40" aria-hidden="true"><path d="M12 10 A15 15 0 1 0 28 10" fill="none" stroke="#ee7470" stroke-width="4" stroke-linecap="round"/><line x1="20" y1="4" x2="20" y2="20" stroke="#ee7470" stroke-width="4" stroke-linecap="round"/></svg>
  <p class="fact" style="left:527px;top:270px;">It Takes The Same Amount<br>Of Energy To Make 1 New<br>Can As It Does To Recycle 20</p>

  <p class="fact" style="left:20px;top:324px;">2/3 Of The Aluminium<br>Ever Produced Is Still In<br>Use Today.</p>
  <div class="fraction"><span>2</span><span>3</span></div>

  <svg class="fact-icon" style="left:484px;top:386px" width="40" height="42" viewBox="0 0 40 42" aria-hidden="true"><rect x="3" y="10" width="34" height="28" rx="4" fill="none" stroke="#4a4b5e" stroke-width="3"/><rect x="8" y="15" width="20" height="18" fill="none" stroke="#4a4b5e" stroke-width="2"/><line x1="13" y1="2" x2="20" y2="9" stroke="#4a4b5e" stroke-width="2"/><line x1="27" y1="2" x2="20" y2="9" stroke="#4a4b5e" stroke-width="2"/></svg>
  <p class="fact" style="left:474px;top:438px;width:200px;">If You Recycled Just One Can Everyday For A Week, You'd Save Enough Energy To Watch Tv Straight For 21 Hours - Thats An Entire Season Of Your Favorite Show</p>

  <p class="fact fact--right" style="left:40px;top:434px;width:124px;">Aluminium Is 100%<br>Recyclable Forever</p>
  <svg class="fact-icon" style="left:177px;top:424px" width="22" height="42" viewBox="0 0 22 42" aria-hidden="true"><rect x="2" y="3" width="18" height="37" rx="3" fill="#ee7470"/><rect x="2" y="16" width="18" height="8" fill="#ffffff" opacity="0.6"/></svg>

  <p class="fact" style="left:180px;top:524px;">A Recycled Can Is Back<br>On The Shelf In 60 Days</p>
  <svg class="fact-icon" style="left:344px;top:522px" width="34" height="34" viewBox="0 0 34 34" aria-hidden="true"><g fill="none" stroke="#a9b83a" stroke-width="4"><path d="M10 8 L17 4 L24 14"/><path d="M28 20 L26 28 L14 28"/><path d="M8 28 L4 22 L10 12"/></g></svg>

  <svg class="cycle" width="260" height="260" viewBox="0 0 260 260" aria-hidden="true">
    <g fill="none" stroke-width="14" stroke-dasharray="100 654">
      <circle cx="130" cy="130" r="120" stroke="#c3c63c" transform="rotate(-114 130 130)"/>
      <circle cx="130" cy="130" r="120" stroke="#ee7470" transform="rotate(-54 130 130)"/>
      <circle cx="130" cy="130" r="120" stroke="#4a4b5e" transform="rotate(6 130 130)"/>
      <circle cx="130" cy="130" r="120" stroke="#c3c63c" transform="rotate(66 130 130)"/>
      <circle cx="130" cy="130" r="120" stroke="#ee7470" transform="rotate(126 130 130)"/>
      <circle cx="130" cy="130" r="120" stroke="#4a4b5e" transform="rotate(186 130 130)"/>
    </g>
  </svg>
  <div class="cycle__text">
    <div class="cycle__lead">TURN YOUR</div>
    <svg class="cycle__dollar" width="32" height="32" viewBox="0 0 32 32" aria-hidden="true"><path d="M6 12 A11 11 0 0 1 24 7" fill="none" stroke="#fff" stroke-width="2.5"/><path d="M26 20 A11 11 0 0 1 8 25" fill="none" stroke="#fff" stroke-width="2.5"/><text x="16" y="21" text-anchor="middle" font-family="Quicksand, sans-serif" font-weight="700" font-size="14" fill="#fff">$</text></svg>
    <div class="cycle__mid">CANS TO</div>
    <div class="cycle__cash">CASH</div>
  </div>

  <div class="scene" role="img" aria-label="Landscape with clouds, sea, rocky cliff, hills and trees"></div>
  <div class="scene__cliff"></div>
  <div class="character" role="img" aria-label="Cartoon boy holding a can, standing on the cliff"></div>
  <div class="coin-badge" role="img" aria-label="Glowing dollar coin with recycling arrows"></div>

  <div class="event">
    <div class="event__row"><span class="event__label">WHEN</span><span class="event__value">Saturday 25th October</span></div>
    <div class="event__row"><span class="event__label">WHERE</span><span class="event__value">12 Harlow Rd Westbrook</span></div>
    <div class="event__row"><span class="event__label">TIME</span><span class="event__value">8am-12pm</span></div>
    <div class="event__row"><span class="event__label">PRIZE</span><span class="event__value">Door Prize Will Be Drawn at 12pm</span></div>
    <div class="event__row"><span class="event__label">PHONE</span><span class="event__value">02 5550 0147 or 1300 555 014</span></div>
  </div>

  <div class="brand">
    <div class="brand__mark"></div>
    <div class="brand__name">PENBURY ORE SERVICES</div>
    <div class="brand__call"><div class="brand__local">LOCAL<br>CALL</div><div class="brand__phone">1300 555 014</div></div>
  </div>
</section>

<!-- A5 flyer, full -->
<section class="flyer flyer--large" aria-label="Cans to cash flyer, full size">
  <div class="flyer__sparkle"></div>
  <div class="headline__win">WIN</div>
  <div class="headline__scooter" role="img" aria-label="Electric scooter illustration"></div>
  <div class="headline__prize">AN ELECTRIC SCOOTER</div>

  <p class="fact" style="left:88px;top:234px;">105,784 Cans Are<br>Recycled Every Minute</p>
  <svg class="fact-icon" style="left:226px;top:228px" width="40" height="40" viewBox="0 0 40 40" aria-hidden="true"><circle cx="20" cy="22" r="14" fill="none" stroke="#c3c63c" stroke-width="3"/><rect x="17" y="3" width="6" height="4" fill="#c3c63c"/><line x1="20" y1="22" x2="27" y2="15" stroke="#c3c63c" stroke-width="3"/></svg>

  <svg class="fact-icon" style="left:470px;top:274px" width="40" height="40" viewBox="0 0 40 40" aria-hidden="true"><path d="M12 10 A15 15 0 1 0 28 10" fill="none" stroke="#ee7470" stroke-width="4" stroke-linecap="round"/><line x1="20" y1="4" x2="20" y2="20" stroke="#ee7470" stroke-width="4" stroke-linecap="round"/></svg>
  <p class="fact" style="left:527px;top:270px;">It Takes The Same Amount<br>Of Energy To Make 1 New<br>Can As It Does To Recycle 20</p>

  <p class="fact" style="left:20px;top:324px;">2/3 Of The Aluminium<br>Ever Produced Is Still In<br>Use Today.</p>
  <div class="fraction"><span>2</span><span>3</span></div>

  <svg class="fact-icon" style="left:484px;top:386px" width="40" height="42" viewBox="0 0 40 42" aria-hidden="true"><rect x="3" y="10" width="34" height="28" rx="4" fill="none" stroke="#4a4b5e" stroke-width="3"/><rect x="8" y="15" width="20" height="18" fill="none" stroke="#4a4b5e" stroke-width="2"/><line x1="13" y1="2" x2="20" y2="9" stroke="#4a4b5e" stroke-width="2"/><line x1="27" y1="2" x2="20" y2="9" stroke="#4a4b5e" stroke-width="2"/></svg>
  <p class="fact" style="left:474px;top:438px;width:200px;">If You Recycled Just One Can Everyday For A Week, You'd Save Enough Energy To Watch Tv Straight For 21 Hours - Thats An Entire Season Of Your Favorite Show</p>

  <p class="fact fact--right" style="left:40px;top:434px;width:124px;">Aluminium Is 100%<br>Recyclable Forever</p>
  <svg class="fact-icon" style="left:177px;top:424px" width="22" height="42" viewBox="0 0 22 42" aria-hidden="true"><rect x="2" y="3" width="18" height="37" rx="3" fill="#ee7470"/><rect x="2" y="16" width="18" height="8" fill="#ffffff" opacity="0.6"/></svg>

  <p class="fact" style="left:180px;top:524px;">A Recycled Can Is Back<br>On The Shelf In 60 Days</p>
  <svg class="fact-icon" style="left:344px;top:522px" width="34" height="34" viewBox="0 0 34 34" aria-hidden="true"><g fill="none" stroke="#a9b83a" stroke-width="4"><path d="M10 8 L17 4 L24 14"/><path d="M28 20 L26 28 L14 28"/><path d="M8 28 L4 22 L10 12"/></g></svg>

  <svg class="cycle" width="260" height="260" viewBox="0 0 260 260" aria-hidden="true">
    <g fill="none" stroke-width="14" stroke-dasharray="100 654">
      <circle cx="130" cy="130" r="120" stroke="#c3c63c" transform="rotate(-114 130 130)"/>
      <circle cx="130" cy="130" r="120" stroke="#ee7470" transform="rotate(-54 130 130)"/>
      <circle cx="130" cy="130" r="120" stroke="#4a4b5e" transform="rotate(6 130 130)"/>
      <circle cx="130" cy="130" r="120" stroke="#c3c63c" transform="rotate(66 130 130)"/>
      <circle cx="130" cy="130" r="120" stroke="#ee7470" transform="rotate(126 130 130)"/>
      <circle cx="130" cy="130" r="120" stroke="#4a4b5e" transform="rotate(186 130 130)"/>
    </g>
  </svg>
  <div class="cycle__text">
    <div class="cycle__lead">TURN YOUR</div>
    <svg class="cycle__dollar" width="32" height="32" viewBox="0 0 32 32" aria-hidden="true"><path d="M6 12 A11 11 0 0 1 24 7" fill="none" stroke="#fff" stroke-width="2.5"/><path d="M26 20 A11 11 0 0 1 8 25" fill="none" stroke="#fff" stroke-width="2.5"/><text x="16" y="21" text-anchor="middle" font-family="Quicksand, sans-serif" font-weight="700" font-size="14" fill="#fff">$</text></svg>
    <div class="cycle__mid">CANS TO</div>
    <div class="cycle__cash">CASH</div>
  </div>

  <div class="scene" role="img" aria-label="Landscape with clouds, sea, rocky cliff, hills and trees"></div>
  <div class="scene__cliff"></div>
  <div class="character" role="img" aria-label="Cartoon boy holding a can, standing on the cliff"></div>
  <div class="coin-badge" role="img" aria-label="Glowing dollar coin with recycling arrows"></div>

  <div class="event">
    <div class="event__row"><span class="event__label">WHEN</span><span class="event__value">Saturday 25th October</span></div>
    <div class="event__row"><span class="event__label">WHERE</span><span class="event__value">12 Harlow Rd Westbrook</span></div>
    <div class="event__row"><span class="event__label">TIME</span><span class="event__value">8am-12pm</span></div>
    <div class="event__row"><span class="event__label">PRIZE</span><span class="event__value">Door Prize Will Be Drawn at 12pm</span></div>
    <div class="event__row"><span class="event__label">PHONE</span><span class="event__value">02 5550 0147 or 1300 555 014</span></div>
  </div>

  <div class="brand">
    <div class="brand__mark"></div>
    <div class="brand__name">PENBURY ORE SERVICES</div>
    <div class="brand__call"><div class="brand__local">LOCAL<br>CALL</div><div class="brand__phone">1300 555 014</div></div>
  </div>
</section>

</body>
</html>
```